Poster for Tradesmen Website

We had a soft launch of our website. The site brings together tradesmen jobseekers and customers to one virtual location. The website serves Australian market. To clearly understand what we mean please visit www.quellmark.com.au. For our future promotional campaign we intend to use poster which we intend to distribute in trade exhibits and in recruitment offices.
Color and Poster Design Content: - Very light blue is the predominant color of the website. The design is not limited on this color. They are free to explore other color if they think that will effectively convey the message of the poster. Presently our website uses images showing tradesmen in action as well as the customers. Designers can use these images or use other image in their design which will best suit their design
Size: - We are looking at poster printed A3 size, but the design should not limit their target size on A3 (it should be versatile, insure that the file format for your design support large-format printing without being pixilated) since we also want it printed in vinyl as stand-alone banner (example: 1200 x 1700 mm approx) that will be used in trade exhibits.
Message of the Poster:
For our first marketing campaign we want to join a trade expo which will be held on the last week of May 2012. For this expo we need a poster and a stand-alone banner to be displayed on our booth. The poster should convey the following message:
a) that a new website has been launched
b) that the website brings together tradesmen, customers and jobseekers to one virtual location
c) that for tradesmen the website is a venue to advertise their business
d) that for customers, it will make the task of finding the right tradies much easier
e) that for jobseekers the site is one way of finding a job by just posting their resume and potential employers can view the summary of their qualification and send notification if they are interested on a particular jobseeker.
Images:
We don't have any other high resolution images Except for the images that we used on our website. We got those images online. Besides, we are not sure what particular image will be appropriate for the poster. As the designer and the creative artist as well, you are free to use whatever images that you think is appropriate for the your design. We think any images (not necessarily tradesmen images) can be used as long as it can strongly convey our message. Again, as the creative artist it is up to you to decide what image is/are appropriate. The only thing we can tell you guys is that we can tell a good/excellent design when we see one.
Logo:
We don't have a logo yet for our website. For the purpose of this poster you can use the font used on website name:
quellmark.com.au
quell {font-family:Arial, Helvetica, sans-serif; color:#407FC0;}
mark.com.au {font-family:Arial, Helvetica, sans-serif; color:#00007F;}
Age group: 18 - 65, Gender: male-female, Education: any
Marketing

```html
<!DOCTYPE html>
<html lang="en">
<head>
<meta charset="utf-8">
<title>QuellMark – Launch Poster</title>
<link rel="stylesheet" href="https://fonts.googleapis.com/css2?family=Arimo:wght@400;700&display=swap">
<style>
  :root {
    --bg: #e4e9f4;
    --paper: #ffffff;
    --red: #d4202a;
    --brand-blue: #3f7fc0;
    --navy: #262a70;
    --ink: #23286a;
    --shadow: rgba(20, 30, 70, 0.35);
  }
  * { box-sizing: border-box; margin: 0; padding: 0; }
  html, body { width: 849px; height: 1200px; overflow: hidden; }
  body {
    position: relative;
    background: var(--bg);
    font-family: "Arimo", Arial, Helvetica, sans-serif;
    color: var(--ink);
  }
  .headline {
    position: absolute; top: 22px; left: 0; width: 849px;
    text-align: center; color: var(--red);
    font-size: 44px; font-weight: 700; letter-spacing: 0.2px; line-height: 1.1;
  }
  .chamfer {
    clip-path: polygon(18px 0, calc(100% - 18px) 0, 100% 18px, 100% calc(100% - 18px), calc(100% - 18px) 100%, 18px 100%, 0 calc(100% - 18px), 0 18px);
  }
  .wordmark-panel {
    position: absolute; left: 29px; top: 83px; width: 793px; height: 159px;
    background: var(--paper);
    display: flex; align-items: center; justify-content: center;
  }
  .wordmark {
    font-size: 146px; font-weight: 700; color: var(--brand-blue);
    letter-spacing: -2px; line-height: 1; white-space: nowrap;
  }
  .photo-strip {
    position: absolute; top: 267px; left: 0; width: 849px; height: 375px;
  }
  .photo { position: absolute; top: 0; height: 100%; }
  .photo--garage { left: 0; width: 233px; background: linear-gradient(160deg, #d7d8d6 0%, #a9a6a2 45%, #b33a36 80%, #3c3a3a 100%); }
  .photo--site { left: 236px; width: 257px; background: linear-gradient(180deg, #c7d3dc 0%, #b9c0c4 45%, #e0b94a 60%, #8b8f95 100%); }
  .photo--home { left: 499px; width: 111px; top: 0; height: 180px; background: linear-gradient(180deg, #e9e7e2, #b7b1a8); }
  .photo--crane { left: 499px; width: 111px; top: 183px; height: 90px; background: linear-gradient(180deg, #f2c94c, #c97f16); }
  .photo--crew { left: 499px; width: 111px; top: 276px; height: 99px; background: linear-gradient(180deg, #c9b9a4, #5d4e43); }
  .photo--plans { left: 613px; width: 236px; background: linear-gradient(200deg, #7a6d61 0%, #e8e8e6 40%, #f0f0ee 60%, #e3b829 85%, #41527c 100%); }

  .card-wrap { position: absolute; filter: drop-shadow(3px 4px 4px var(--shadow)); }
  .card {
    width: 100%; height: 100%;
    background: var(--paper);
    clip-path: polygon(0 0, calc(100% - 20px) 0, 100% 20px, 100% 100%, 0 100%);
  }
  .card--intro { padding: 8px 12px 0 13px; }
  .intro-text { font-size: 36px; font-weight: 700; line-height: 43px; color: var(--ink); }
  .intro-text .brand { color: var(--brand-blue); }
  .card--info { padding: 10px 14px; }
  .card-title { color: var(--red); font-size: 27px; font-weight: 700; line-height: 1.15; letter-spacing: 1.5px; }
  .card-body { font-size: 21px; line-height: 28.5px; color: var(--ink); font-weight: 400; white-space: nowrap; }
  .card--job .card-body { font-size: 20.5px; line-height: 27px; }

  .url-band {
    position: absolute; left: 31px; top: 1103px; width: 789px; height: 62px;
    background: var(--navy);
    display: flex; align-items: center; justify-content: center;
    color: #ffffff; font-size: 58px; font-weight: 700; letter-spacing: 0.5px; line-height: 1;
  }
</style>
</head>
<body>
  <h1 class="headline">A new website has been launched</h1>

  <div class="wordmark-panel chamfer">
    <span class="wordmark">QuellMark</span>
  </div>

  <div class="photo-strip">
    <div class="photo photo--garage" role="img" aria-label="Mechanic working under the bonnet of a red car while a customer waits"></div>
    <div class="photo photo--site" role="img" aria-label="Collage of construction workers in hard hats reviewing plans on a building site"></div>
    <div class="photo photo--home" role="img" aria-label="Plumber fixing a kitchen sink for a homeowner"></div>
    <div class="photo photo--crane" role="img" aria-label="Silhouetted builders and a crane against a golden sky"></div>
    <div class="photo photo--crew" role="img" aria-label="Worker in an orange hard hat on site"></div>
    <div class="photo photo--plans" role="img" aria-label="Client and tradesman shaking hands over building plans"></div>
  </div>

  <div class="card-wrap" style="left:29px; top:668px; width:236px; height:401px;">
    <div class="card card--intro">
      <p class="intro-text"><span class="brand">QuellMark</span><br>brings<br>together<br>tradesmen,<br>customers<br>and job-<br>seekers to<br>one virtual<br>location.</p>
    </div>
  </div>

  <div class="card-wrap" style="left:302px; top:668px; width:244px; height:167px;">
    <div class="card card--info">
      <h2 class="card-title">TRADESMEN</h2>
      <p class="card-body">The website is a<br>venue to advertise/<br>promote your<br>business.</p>
    </div>
  </div>

  <div class="card-wrap" style="left:575px; top:668px; width:247px; height:167px;">
    <div class="card card--info">
      <h2 class="card-title">CUSTOMERS</h2>
      <p class="card-body">The website makes<br>the task of finding<br>the right tradies<br>much easier.</p>
    </div>
  </div>

  <div class="card-wrap" style="left:302px; top:873px; width:520px; height:196px;">
    <div class="card card--info card--job">
      <h2 class="card-title">FIND A JOB</h2>
      <p class="card-body">The website is one way of finding a job<br>by just posting their resume and potential<br>employers can view the summary of their<br>qualification and send notification if they<br>are interested on a particular jobseeker.</p>
    </div>
  </div>

  <div class="url-band chamfer">www.quellmark.com.au</div>
</body>
</html>
```